Business card design needed

i am a small sized carpentry business looking to generate work in decks, pergolas, small renovations including bathroom renovations or overseeing new homes being built.

Carpentry

R K Carpentry
Marcus Ellery
0417382906
Specialize in quality decks, pergolas, small renovations including bathrooms and housing project management.
FREE QUOTES

```html
<!DOCTYPE html>
<html lang="en">
<head>
<meta charset="utf-8">
<title>R K Carpentry – Business Card</title>
<link rel="stylesheet" href="https://fonts.googleapis.com/css2?family=Open+Sans:wght@400&family=PT+Sans:wght@400;700&display=swap">
<style>
  :root {
    --wood-light: #efe6a2;
    --wood-mid: #d6c866;
    --wood-deep: #b4a13a;
    --band: rgba(255, 250, 225, 0.30);
    --brown: #7f5e08;
    --white: #ffffff;
    --shadow: rgba(60, 40, 0, 0.5);
  }
  html, body {
    margin: 0;
    padding: 0;
    width: 1200px;
    height: 741px;
    overflow: hidden;
    background: #ffffff;
  }
  .card {
    position: relative;
    width: 1200px;
    height: 741px;
    overflow: hidden;
  }
  .wood-surface {
    position: absolute;
    inset: 0;
    background:
      radial-gradient(ellipse 60% 40% at 62% 18%, rgba(255,252,220,0.45), rgba(255,252,220,0) 70%),
      linear-gradient(90deg, var(--wood-deep) 0%, var(--wood-mid) 18%, var(--wood-light) 45%, var(--wood-mid) 70%, var(--wood-light) 85%, var(--wood-mid) 100%);
  }
  .center-band {
    position: absolute;
    left: 344px;
    top: 0;
    width: 508px;
    height: 741px;
    background: var(--band);
  }
  .services {
    position: absolute;
    left: 344px;
    width: 508px;
    top: 0;
    margin: 0;
    padding: 0;
    list-style: none;
    font-family: "PT Sans", sans-serif;
    font-weight: 700;
    color: var(--brown);
    font-size: 42px;
    letter-spacing: 3px;
    text-align: center;
    text-shadow: 2px 2px 3px var(--shadow);
  }
  .services li {
    position: absolute;
    left: 0;
    right: 0;
    line-height: 1;
    white-space: nowrap;
  }
  .services li:nth-child(1) { top: 33px; }
  .services li:nth-child(2) { top: 96px; }
  .services li:nth-child(3) { top: 160px; }
  .services li:nth-child(4) { top: 231px; }
  .business-name {
    position: absolute;
    left: 0;
    top: 0;
    width: 1200px;
    height: 741px;
  }
  .business-name text {
    font-family: "Open Sans", sans-serif;
    font-weight: 400;
    font-size: 245px;
    fill: var(--brown);
  }
  .contact {
    position: absolute;
    left: 344px;
    width: 508px;
    top: 600px;
    text-align: center;
    font-family: "PT Sans", sans-serif;
    color: var(--white);
    font-size: 44px;
    letter-spacing: 2px;
    line-height: 62px;
    text-shadow: 1px 1px 3px var(--shadow);
  }
  .contact p { margin: 0; }
</style>
</head>
<body>
  <main class="card">
    <div class="wood-surface" role="img" aria-label="Golden timber surface background"></div>
    <div class="center-band"></div>

    <ul class="services">
      <li>DECKS</li>
      <li>PERGOLAS</li>
      <li>SMALL RENOVATIONS</li>
      <li>HOUSING PROJECT</li>
    </ul>

    <svg class="business-name" viewBox="0 0 1200 741" aria-label="R K Carpentry">
      <text x="10" y="455" textLength="1168" lengthAdjust="spacingAndGlyphs">R K Carpentry</text>
    </svg>

    <div class="contact">
      <p class="contact-name">Marcus Ellery</p>
      <p class="contact-phone">0417382906</p>
    </div>
  </main>
</body>
</html>
```